Design business cards for startup

Company Name: Lumen Trek

Look at the company logo and use it to design business cards (front & back) for my company.
My company is a startup provide wonderful service for Americans traveling to China.
The business cards should be creative and succinct.
Here is the website of my company www.lumentrekko.com. You can find more resource and information in the website.

Also please ensure to leave sufficient space for me to insert text later on.

Thank you for participating.

```html
<!DOCTYPE html>
<html lang="en">
<head>
<meta charset="utf-8">
<title>Lumen Trek — Business Cards</title>
<link rel="stylesheet" href="https://fonts.googleapis.com/css2?family=Raleway:wght@300;400;600;700&display=swap">
<style>
  :root {
    --backdrop: #2c3a42;
    --card-dark: #343536;
    --photo-light: #e3b752;
    --photo-mid: #b98a2c;
    --photo-deep: #6e4a1c;
    --accent: #e98a2a;
    --ink-light: #f2f2f2;
    --ink-soft: #d6d6d6;
  }
  * { box-sizing: border-box; margin: 0; padding: 0; }
  html, body {
    width: 1200px; height: 900px; overflow: hidden;
    background: var(--backdrop);
    font-family: "Raleway", sans-serif;
  }
  .sheet {
    width: 1200px; height: 900px;
    display: flex; flex-direction: column; align-items: center; justify-content: center;
    gap: 40px;
  }
  .card {
    position: relative;
    width: 700px; height: 400px;
    box-shadow: 0 10px 30px rgba(0,0,0,0.35);
    overflow: hidden;
  }
  /* Front */
  .card-front .photo {
    position: absolute; inset: 0;
    background:
      linear-gradient(180deg, var(--photo-light) 0%, var(--photo-mid) 30%, var(--photo-deep) 55%, var(--photo-mid) 70%, var(--photo-light) 100%);
  }
  .card-front .url {
    position: absolute; left: 26px; bottom: 30px;
    color: var(--ink-light); font-size: 11px; letter-spacing: 2.5px; font-weight: 400;
  }
  .card-front .brand {
    position: absolute; right: 30px; bottom: 34px;
    color: var(--ink-light); font-size: 26px; font-weight: 700; letter-spacing: 1px;
    text-transform: uppercase;
  }
  /* Back */
  .card-back { background: var(--card-dark); }
  .card-back .brand-block {
    position: absolute; left: 0; top: 0; width: 340px; height: 100%;
    display: flex; align-items: center; justify-content: center; gap: 14px;
  }
  .card-back .brand-dot {
    width: 30px; height: 30px; border-radius: 50%; background: var(--accent);
  }
  .card-back .brand-name {
    color: var(--accent); font-size: 34px; font-weight: 700; letter-spacing: 1px;
    text-transform: uppercase;
  }
  .card-back .divider {
    position: absolute; left: 340px; top: 50px; width: 2px; height: 300px;
    background: var(--accent);
  }
  .card-back .details {
    position: absolute; left: 380px; top: 68px;
  }
  .card-back .person {
    color: var(--accent); font-size: 24px; font-weight: 300; text-transform: uppercase;
    letter-spacing: 0.5px; margin-bottom: 38px;
  }
  .card-back .contact {
    color: var(--ink-soft); font-size: 15px; line-height: 1.35; font-weight: 400;
  }
  .card-back .contact-url {
    margin-top: 52px;
    color: var(--ink-light); font-size: 11px; letter-spacing: 2.5px;
  }
</style>
</head>
<body>
  <main class="sheet">
    <section class="card card-front" aria-label="Card front">
      <div class="photo" role="img" aria-label="Warm golden photograph of a traditional Chinese palace hall with stone balustrades"></div>
      <p class="url">www.lumentrekko.com</p>
      <p class="brand">Lumen Trek</p>
    </section>

    <section class="card card-back" aria-label="Card back">
      <div class="brand-block">
        <span class="brand-dot"></span>
        <span class="brand-name">Lumen Trek</span>
      </div>
      <div class="divider"></div>
      <div class="details">
        <h1 class="person">Daniel Reyes</h1>
        <p class="contact">555-201-3384<br>Daniel.R@lumentrekko.com</p>
        <p class="contact-url">www.lumentrekko.com</p>
      </div>
    </section>
  </main>
</body>
</html>
```